3 pages of UI design for AdTech Startup

We need 3 pages of UI design for a new AdTech company located in Seattle called KESTREL Systems.

We put digital, mobile billboards on college campuses throughout the country. This design project involves our back-end customer dashboard.

Page 1- Dashboard home page
page 2- Manage ads screen (see File 3 below for the screenshot of our current design). Please match the design of all 3 screens so there is consistency
page 3-Detailed Zone screen (see file 16 below). This page looks similar to the first page but gives a more detailed overview and a larger map.

The features and functionality are already built but we are lacking an aesthetically pleasing and slick design. Looking for someone who can match our website look to this new dashboard space. Our company reflects modern, clean, elegant design that is straight-forward and user friendly (main inspiration is VOLTA, we love their design and feel).

Target Market(s)

-Local business owner, marketing directors, and national advertising and marketing agencies

Industry/Entity Type

Advertising

Number of Pages Required

3 page

Font styles to use
Other font styles liked:
• Proxima Nova- Thin for body text, Light for title

Colors
85cae6
33a6d7
0292cd
ffffff

Requirements
Nice to have
• Please include enough detail so that my developer can look at the design you come up with and translate it to html. Please include spacing, fonts, color numbers. My developer is going to look at your creation and recreate it in html format

```html
<!DOCTYPE html>
<html lang="en">
<head>
<meta charset="utf-8">
<title>KESTREL Systems — Dashboard</title>
<link href="https://fonts.googleapis.com/css2?family=Roboto:wght@300;400;500;700&display=swap" rel="stylesheet">
<style>
:root{
  --sky:#85cae6;
  --brand:#33a6d7;
  --brand-deep:#0292cd;
  --band:#3bb3e4;
  --white:#ffffff;
  --ink:#333333;
  --muted:#8c8c8c;
  --line:#d6d6d6;
  --bg-a:#9a9a9a;
  --bg-b:#7d7d7d;
  --yellow:#f4c443;
  --red:#ee6a5b;
  --blue:#5f9ed8;
  --grey-ring:#9c9c9c;
  --dark:#2b2b2b;
}
*{box-sizing:border-box;margin:0;padding:0}
html,body{width:1200px;height:741px;overflow:hidden}
body{font-family:'Roboto',Arial,sans-serif;color:var(--ink);background:var(--bg-b)}
.stage{position:absolute;left:0;top:0;width:1400px;height:864px;transform:scale(0.857143);transform-origin:0 0;
  background:linear-gradient(135deg,var(--bg-a) 0%,var(--bg-b) 55%,var(--bg-a) 100%)}
.abs{position:absolute}

/* header */
.topbar{position:absolute;left:0;top:0;width:1400px;height:98px;background:var(--white)}
.brand{position:absolute;left:115px;top:36px;display:flex;align-items:center;gap:10px;color:var(--brand);font-size:30px;font-weight:300;letter-spacing:1px}
.brand-square{width:18px;height:18px;background:var(--brand)}
.client-name{position:absolute;left:770px;top:35px;font-size:26px;font-weight:700;color:#1d4e9e;letter-spacing:.5px}
.pill{position:absolute;top:33px;height:36px;border:1px solid #cfcfcf;border-radius:18px;display:flex;align-items:center;font-size:15px;color:var(--ink);background:var(--white)}
.pill.search{left:858px;width:37px;justify-content:center}
.pill.user{left:907px;width:150px;padding-left:2px;gap:8px}
.avatar{width:32px;height:32px;border-radius:50%;background:linear-gradient(#b9b2aa,#6d655e)}
.caret{width:0;height:0;border-left:5px solid transparent;border-right:5px solid transparent;border-top:6px solid #444;margin-left:6px}
.pill.help{left:1064px;width:99px;padding-left:12px;gap:10px;font-weight:700}
.pill.logout{left:1172px;width:110px;padding-left:12px;gap:10px;font-weight:700}

/* panels */
.panel{position:absolute;background:var(--white)}
.panel-head{height:50px;background:var(--band);color:var(--white);font-size:20px;font-weight:400;display:flex;align-items:center;padding-left:18px}
.rotations{left:114px;top:128px;width:849px;height:399px}
.help-panel{left:977px;top:128px;width:308px;height:399px}
.zones{left:114px;top:558px;width:779px;height:269px}
.zone-perf{left:908px;top:558px;width:379px;height:269px}

.date-range{position:absolute;left:583px;top:11px;width:249px;height:30px;background:var(--white);display:flex;font-size:14px;color:#555;letter-spacing:.5px}
.date-range span{flex:1;display:flex;align-items:center;justify-content:center;gap:8px}
.date-range span+span{border-left:1px solid var(--line)}
.cal{width:15px;height:14px;border:1.5px solid var(--brand);border-top-width:4px;border-radius:2px}

.range-toggle{position:absolute;left:588px;top:58px;height:30px;display:flex;border:1px solid var(--brand-deep);font-size:14px;color:#555}
.range-toggle span{display:flex;align-items:center;justify-content:center;border-left:1px solid var(--line)}
.range-toggle span:first-child{border-left:0}
.range-toggle .on{background:var(--brand-deep);color:var(--white);font-weight:500}

.chart{position:absolute;left:0;top:50px;width:849px;height:349px}

/* stat rings */
.stat{position:absolute;text-align:center;width:140px}
.stat svg{display:block;margin:0 auto}
.stat .label{font-size:16px;color:var(--ink);margin-top:10px}
.zone-perf .stat .label{color:var(--muted);font-size:16px;margin-top:6px}

/* zone table */
.zone-head{display:flex;height:50px;background:var(--band);color:var(--white);font-size:20px}
.zone-head div,.zone-body>div{display:flex;justify-content:center}
.zone-head div{align-items:center}
.col-zone{width:146px}
.col-active{width:151px;border-left:1px solid var(--white)}
.col-path{flex:1;border-left:1px solid var(--white)}
.zone-body{display:flex;height:219px}
.zone-body .col-active,.zone-body .col-path{border-left:1px solid #e4e4e4}
.zone-name{text-align:center;padding-top:48px;font-size:15px}
.zone-name strong{display:block;color:var(--brand-deep);font-weight:400;font-size:20px;margin-bottom:2px}
.active-cell{flex-direction:column;align-items:center;padding-top:20px}
.venue-photo{width:125px;height:98px;border-radius:3px;background:linear-gradient(160deg,#3b2a22 0%,#c7773d 45%,#e2a75c 60%,#2a2220 100%)}
.btn{display:flex;align-items:center;justify-content:center;color:var(--white);font-size:17px;background:var(--brand-deep)}
.manage{width:125px;height:34px;margin-top:21px}
.map{position:relative;margin-top:20px;width:450px;height:159px;border-radius:6px;background:linear-gradient(135deg,#7d8a5a 0%,#9aa07a 40%,#8d8f86 70%,#6f7668 100%);overflow:hidden}
.map-card{position:absolute;left:0;top:6px;width:293px;height:54px;background:var(--white);padding:8px 20px;box-shadow:0 1px 3px rgba(0,0,0,.3)}
.map-card b{display:block;font-weight:400;font-size:17px;color:#333}
.map-card small{font-size:12px;color:#3a7bd5}
.map-card .star{position:absolute;right:20px;top:8px;color:#aaa;font-size:17px}

.perf-actions{position:absolute;left:86px;top:214px;display:flex;gap:4px}
.perf-actions .btn{height:34px;font-size:15px}
.perf-actions .texts{width:127px}
.perf-actions .details{width:80px;background:var(--dark);height:34px}
</style>
</head>
<body>
<div class="stage">

  <header class="topbar">
    <div class="brand"><span class="brand-square"></span>KESTREL</div>
    <div class="client-name">CAPRA</div>
    <div class="pill search">
      <svg width="18" height="18" viewBox="0 0 18 18"><circle cx="7.5" cy="7.5" r="5.5" fill="none" stroke="#0292cd" stroke-width="2.2"/><line x1="11.5" y1="11.5" x2="16" y2="16" stroke="#0292cd" stroke-width="2.4" stroke-linecap="round"/></svg>
    </div>
    <div class="pill user"><span class="avatar" role="img" aria-label="User profile photo"></span>Jordan Pell<span class="caret"></span></div>
    <div class="pill help">
      <svg width="22" height="22" viewBox="0 0 22 22"><circle cx="11" cy="11" r="11" fill="#0292cd"/><text x="11" y="16" text-anchor="middle" font-family="Roboto,sans-serif" font-weight="700" font-size="14" fill="#fff">?</text></svg>Help
    </div>
    <div class="pill logout">
      <svg width="22" height="20" viewBox="0 0 22 20"><rect x="1" y="1" width="11" height="18" rx="1" fill="#85cae6"/><path d="M9 10h9M15 6l4 4-4 4" stroke="#0292cd" stroke-width="2.4" fill="none"/></svg>Logout
    </div>
  </header>

  <section class="panel rotations">
    <div class="panel-head">AD ROTATIONS</div>
    <div class="date-range"><span><i class="cal"></i>25/06/2016</span><span><i class="cal"></i>25/07/2016</span></div>
    <div class="range-toggle">
      <span style="width:69px">Hourly</span><span class="on" style="width:50px">Day</span><span style="width:62px">Week</span><span style="width:67px">Month</span>
    </div>
    <svg class="chart" viewBox="114 178 849 349" width="849" height="349">
      <defs>
        <pattern id="stripes" width="10" height="5.5" patternUnits="userSpaceOnUse">
          <rect width="10" height="3.5" fill="#6fc6ec"/>
        </pattern>
      </defs>
      <g font-family="Roboto,sans-serif" font-size="15" fill="#333" text-anchor="end">
        <text x="147" y="232">100</text><text x="147" y="291">75</text><text x="147" y="349">50</text><text x="147" y="407">25</text><text x="147" y="464">0</text>
      </g>
      <line x1="162" y1="222" x2="162" y2="462" stroke="#aaa"/>
      <line x1="162" y1="462" x2="942" y2="462" stroke="#aaa"/>
      <g stroke="#777">
        <line x1="211" y1="462" x2="211" y2="470"/><line x1="309" y1="462" x2="309" y2="470"/><line x1="406" y1="462" x2="406" y2="470"/><line x1="508" y1="462" x2="508" y2="470"/><line x1="613" y1="462" x2="613" y2="470"/><line x1="716" y1="462" x2="716" y2="470"/><line x1="820" y1="462" x2="820" y2="470"/><line x1="925" y1="462" x2="925" y2="470"/>
      </g>
      <g fill="url(#stripes)">
        <rect x="193" y="396" width="36" height="66"/><rect x="291" y="346" width="36" height="116"/><rect x="388" y="360" width="36" height="102"/><rect x="490" y="329" width="36" height="133"/><rect x="595" y="349" width="36" height="113"/><rect x="698" y="299" width="36" height="163"/><rect x="802" y="309" width="36" height="153"/><rect x="907" y="280" width="36" height="182"/>
      </g>
      <g fill="#74cbee">
        <rect x="193" y="443" width="36" height="19"/><rect x="291" y="405" width="36" height="57"/><rect x="388" y="408" width="36" height="54"/><rect x="490" y="377" width="36" height="85"/><rect x="595" y="398" width="36" height="64"/><rect x="698" y="346" width="36" height="116"/><rect x="802" y="358" width="36" height="104"/><rect x="907" y="328" width="36" height="134"/>
      </g>
      <polyline points="190,446 288,410 387,408 487,378 592,398 695,348 799,358 905,328" fill="none" stroke="#1a9bd3" stroke-width="1.2"/>
      <g fill="#fff" stroke="#1a9bd3" stroke-width="2">
        <circle cx="190" cy="446" r="3.5"/><circle cx="288" cy="410" r="3.5"/><circle cx="387" cy="408" r="3.5"/><circle cx="487" cy="378" r="3.5"/><circle cx="592" cy="398" r="3.5"/><circle cx="695" cy="348" r="3.5"/><circle cx="799" cy="358" r="3.5"/><circle cx="905" cy="328" r="3.5"/>
      </g>
      <g font-family="Roboto,sans-serif" font-size="13" font-weight="700" fill="#333" text-anchor="middle">
        <text x="212" y="508">Jul 29,2016</text><text x="307" y="508">Jul 30,2016</text><text x="404" y="508">Jul 31,2016</text><text x="504" y="508">Aug 01,2016</text><text x="607" y="508">Aug 02,2016</text><text x="710" y="508">Aug 03,2016</text><text x="813" y="508">Aug 04,2016</text><text x="916" y="508">Aug 05,2016</text>
      </g>
    </svg>
  </section>

  <section class="panel help-panel">
    <div class="panel-head">Help</div>
    <div class="stat" style="left:1px;top:76px">
      <svg width="90" height="90" viewBox="-45 -45 90 90"><circle r="44" fill="#e6e6e6" stroke="var(--grey-ring)" stroke-width="1"/><path d="M0 0L0-44A44 44 0 0 1 35.6-25.9Z" fill="#fff"/><text y="7" text-anchor="middle" font-family="Roboto,sans-serif" font-size="21" font-weight="300" fill="#999">85%</text></svg>
      <div class="label">Rotations</div>
    </div>
    <div class="stat" style="left:159px;top:76px">
      <svg width="90" height="90" viewBox="-45 -45 90 90"><circle r="44" fill="#fff" stroke="var(--yellow)" stroke-width="1.5"/><path d="M0 0H-44M0 0L20 38" stroke="var(--yellow)" stroke-width="1"/><text y="4" text-anchor="middle" font-family="Roboto,sans-serif" font-size="21" font-weight="300" fill="#999">21:25</text><text y="23" text-anchor="middle" font-family="Roboto,sans-serif" font-size="14" font-weight="300" fill="#999">min</text></svg>
      <div class="label">Time</div>
    </div>
    <div class="stat" style="left:1px;top:234px">
      <svg width="90" height="90" viewBox="-45 -45 90 90"><circle r="44" fill="#fff" stroke="var(--red)" stroke-width="1.5"/><text y="7" text-anchor="middle" font-family="Roboto,sans-serif" font-size="21" font-weight="300" fill="#999">595</text></svg>
      <div class="label">Impressions</div>
    </div>
    <div class="stat" style="left:159px;top:234px">
      <svg width="90" height="90" viewBox="-45 -45 90 90"><circle r="44" fill="#fff" stroke="var(--blue)" stroke-width="1.5"/><text y="7" text-anchor="middle" font-family="Roboto,sans-serif" font-size="21" font-weight="300" fill="#999">0.3</text></svg>
      <div class="label">Miles</div>
    </div>
  </section>

  <section class="panel zones">
    <div class="zone-head"><div class="col-zone">ZONE</div><div class="col-active">ACTIVE</div><div class="col-path">CARRIER PARTH</div></div>
    <div class="zone-body">
      <div class="col-zone"><div class="zone-name"><strong>Zone 1</strong>Harlow's House</div></div>
      <div class="col-active active-cell">
        <div class="venue-photo" role="img" aria-label="Photo of an indoor basketball arena during a game"></div>
        <div class="btn manage">Manage</div>
      </div>
      <div class="col-path">
        <div class="map" role="img" aria-label="Satellite map of the carrier path around Harlow's House">
          <div class="map-card"><b>Harlow's House</b><small>View larger map</small><span class="star">★</span></div>
        </div>
      </div>
    </div>
  </section>

  <section class="panel zone-perf">
    <div class="panel-head" style="justify-content:center;padding-left:0">ZONE PERFORMANCE</div>
    <div class="stat" style="left:-2px;top:72px">
      <svg width="90" height="90" viewBox="-45 -45 90 90"><circle r="44" fill="#e6e6e6" stroke="var(--grey-ring)" stroke-width="1"/><path d="M0 0L0-44A44 44 0 0 1 35.6-25.9Z" fill="#fff"/><text y="7" text-anchor="middle" font-family="Roboto,sans-serif" font-size="21" font-weight="300" fill="#999">85%</text></svg>
      <div class="label">Rotations</div>
    </div>
    <div class="stat" style="left:111px;top:72px">
      <svg width="90" height="90" viewBox="-45 -45 90 90"><circle r="44" fill="#fff" stroke="var(--yellow)" stroke-width="1.5"/><path d="M0 0H-44M0 0L20 38" stroke="var(--yellow)" stroke-width="1"/><text y="4" text-anchor="middle" font-family="Roboto,sans-serif" font-size="21" font-weight="300" fill="#999">21:25</text><text y="23" text-anchor="middle" font-family="Roboto,sans-serif" font-size="14" font-weight="300" fill="#999">min</text></svg>
      <div class="label">Broadcast time</div>
    </div>
    <div class="stat" style="left:238px;top:72px">
      <svg width="90" height="90" viewBox="-45 -45 90 90"><circle r="44" fill="#fff" stroke="var(--blue)" stroke-width="1.5"/><text y="7" text-anchor="middle" font-family="Roboto,sans-serif" font-size="21" font-weight="300" fill="#999">0.3</text></svg>
      <div class="label">Miles Walked</div>
    </div>
    <div class="perf-actions"><div class="btn texts">Text Messages</div><div class="btn details">Details</div></div>
  </section>

</div>
</body>
</html>
```